Verdanix Medical Business Card

Create a high class Business card for Medical Aesthetics and Wellness Practice called Verdanix Medical Aesthetics and Wellness as per the logo attached.
Addresss is: 418 Harlan Brook Road Suite 312 Melville, New York 11093
Phone (555)204-7391 IG @verdanix_medical
Verdanixmedical.example

I need 5 different name configurations
1) Dr. Theo Valcourt
Aesthetics and Wellness Specialist
Medical Director

2) Rosalind Pettinger, NP
Clinical Nurse Manager

3) Marla Vostrik, RN
Aesthetic Nurse Specialist

4) Petra Halvesen, RN

5) Dana Kowbeck, L.E.
Senior Licensed Esthetician

Target Market(s)

22-55 Females

Industry/Entity Type

Medical Spa and Wellness

Contact Information for Business Card

Logo, address, phone, web, instagram, providers name

Requirements
Must have
• Attractive classy modern look

```html
<!DOCTYPE html>
<html lang="en">
<head>
<meta charset="utf-8">
<title>Verdanix Medical – Business Card</title>
<link rel="stylesheet" href="https://fonts.googleapis.com/css2?family=Montserrat:wght@400;600&display=swap">
<style>
  :root {
    --page: #ffffff;
    --board: #071b1a;
    --teal: #114f60;
    --ink: #124d5e;
    --text: #1f3a44;
    --white: #ffffff;
  }
  * { margin: 0; padding: 0; box-sizing: border-box; }
  html, body {
    width: 1200px; height: 1000px; overflow: hidden;
    background: var(--page);
  }
  .board {
    position: absolute; left: 333px; top: 142px;
    width: 535px; height: 715px;
    background: var(--board);
  }
  .card {
    position: absolute; left: 34px;
    width: 465px; height: 265px;
    overflow: hidden;
  }
  .card--front { top: 36px; background: var(--white); }
  .card--back { top: 414px; background: var(--teal); }

  .brand-name {
    position: absolute; text-align: center;
    font-family: "Montserrat", sans-serif; font-weight: 400;
  }
  .card--front .brand-name {
    left: 16px; top: 142px; width: 180px;
    font-size: 14px; line-height: 21px; color: var(--ink);
  }
  .card--back .brand-name {
    left: 72px; top: 100px; width: 320px;
    font-size: 22px; line-height: 32px; color: var(--white);
  }

  .person {
    position: absolute; left: 227px; top: 30px;
    font-family: "Montserrat", sans-serif; color: var(--ink);
  }
  .person__name { font-size: 21.5px; font-weight: 600; line-height: 1.2; }
  .person__role { font-size: 11px; font-weight: 400; line-height: 15px; color: var(--text); margin-left: 1px; }
  .person__role:first-of-type { margin-top: 2px; }

  .contacts {
    position: absolute; left: 227px; top: 128px;
    list-style: none;
    font-family: "Montserrat", sans-serif; font-size: 10.5px; color: var(--text);
  }
  .contacts li { display: flex; align-items: center; height: 18.3px; }
  .contacts svg { width: 14px; height: 14px; margin-right: 9px; flex: none; }

  .address {
    position: absolute; left: 0; top: 218px; width: 465px; text-align: center;
    font-family: "Montserrat", sans-serif; font-size: 12.4px; color: var(--ink);
  }
  .wave { position: absolute; left: 0; top: 240px; width: 465px; height: 25px; display: block; }
</style>
</head>
<body>
  <div class="board">
    <section class="card card--front">
      <p class="brand-name">Verdanix Medical Aesthetics and Wellness</p>

      <div class="person">
        <div class="person__name">Dr. Theo Valcourt</div>
        <div class="person__role">Aesthetics and Wellness Specialist</div>
        <div class="person__role">Medical Director</div>
      </div>

      <ul class="contacts">
        <li>
          <svg viewBox="0 0 24 24" aria-hidden="true"><path fill="#124d5e" d="M6.6 10.8a15.1 15.1 0 0 0 6.6 6.6l2.2-2.2a1 1 0 0 1 1-.25 11.4 11.4 0 0 0 3.6.57 1 1 0 0 1 1 1V20a1 1 0 0 1-1 1A17 17 0 0 1 3 4a1 1 0 0 1 1-1h3.5a1 1 0 0 1 1 1c0 1.25.2 2.45.57 3.57a1 1 0 0 1-.25 1z"/><path fill="none" stroke="#124d5e" stroke-width="1.8" d="M14 2.5a8 8 0 0 1 7.5 7.5M14 6a4.5 4.5 0 0 1 4 4"/></svg>
          (555)204-7391
        </li>
        <li>
          <svg viewBox="0 0 24 24" aria-hidden="true"><rect x="1" y="4" width="22" height="16" fill="#124d5e"/><path fill="none" stroke="#fff" stroke-width="1.6" d="M1.5 5l10.5 8 10.5-8M1.5 19.5l8-7M22.5 19.5l-8-7"/></svg>
          tmorrow@lumerahealth.example
        </li>
        <li>
          <svg viewBox="0 0 24 24" aria-hidden="true"><rect x="2" y="2" width="20" height="20" rx="5" fill="#124d5e"/></svg>
          @verdanix_medical
        </li>
        <li>
          <svg viewBox="0 0 24 24" aria-hidden="true"><circle cx="12" cy="12" r="10.5" fill="#124d5e"/><g fill="none" stroke="#fff" stroke-width="1.2"><ellipse cx="12" cy="12" rx="4.5" ry="10.5"/><path d="M1.5 12h21M3 7h18M3 17h18M12 1.5v21"/></g></svg>
          Verdanixmedical.example
        </li>
      </ul>

      <p class="address">418 Harlan Brook Road Suite 312 Melville, New York 11093</p>

      <svg class="wave" viewBox="0 0 465 25" preserveAspectRatio="none" aria-hidden="true">
        <path fill="#114f60" d="M0 17H258C284 17 292 2 322 2H465V25H0Z"/>
        <path fill="none" stroke="#ffffff" stroke-width="3" d="M0 15.5H257C282 15.5 290 1 320 0.5"/>
        <path fill="#114f60" d="M0 7H279C272 11 266 12.5 258 12.5H0Z"/>
      </svg>
    </section>

    <section class="card card--back">
      <p class="brand-name">Verdanix Medical Aesthetics and Wellness</p>
    </section>
  </div>
</body>
</html>
```